Webdesign für Baucoaching-Unternehmen
Ist sehr offen und ehrlich und steht zu seinen Design‘s. Mit Ihm könnt Ihr gut zusammen arbeiten und erhalten die Visualisierung gleich als Vorschlag. ... er hat kurzerhand eine eine Seite erstellt.
Zielgruppe
Die PRT Design bietet Baucoaching an.
Unsere Zielgruppe sind Privatkunden die Planen eine Immobilie zu erwerben.
Was machen wir:
Wie im Coaching üblich starten wir mit einer ist Analyse. wie wohnen Sie zur Zeit
Gehen dann weiter in die Planung. Was darf sich in Zukunft ändern.
In den nächsten Schritten Formulieren wir die Zukunft weiter aus und ergänzen diese Mit Zahlen. Die erste Kalkulation wird erstellt.
So geht es weiter bis zum Baubeginn.
Wenn gewünscht prüfen wir während der Bauphase ob alle Punkte aus der Vorbesprechung eingehalten werden.
Abschluss unserer Arbeit ist der der Einzug.
Aufgabenstellung
Es gibt schon eine Visitenkarte und ich habe mir schon mal grundsätzlich Gedanken zum Aufbau gemacht.
Das Logo und die Visitenkarte wurden auch auf Entwurfsbörse erstellt. Leider komme ich nicht an die Daten ran. Hat einer von euch eine Idee ? Danke Jonas Brulin

```html
<!DOCTYPE html>
<html lang="de">
<head>
<meta charset="utf-8">
<title>PRT Design – Baucoaching</title>
<link href="https://fonts.googleapis.com/css2?family=Open+Sans:ital,wght@0,300;0,400;0,600;0,700;1,600&family=Roboto:wght@400;500&display=swap" rel="stylesheet">
<style>
:root{
  --green:#4bb04f;
  --text:#3a3a3a;
  --footer:#262626;
  --footer-text:#e6e6e6;
  --footer-muted:#8a8a8a;
}
*{box-sizing:border-box;margin:0;padding:0}
html,body{width:1200px;height:3341px;overflow:hidden}
body{position:relative;background:#fff;font-family:"Open Sans",sans-serif;color:var(--text)}
.abs{position:absolute}
.nav{left:0;top:0;width:1200px;height:40px;border-bottom:1px solid #eee;background:#fff;box-shadow:0 1px 3px rgba(0,0,0,.06)}
.brand{left:19px;top:8px;display:flex;align-items:center;gap:6px;font-weight:700;font-size:14px;color:#444}
.brand .dot{width:24px;height:24px;border-radius:50%;background:#6d6d6d}
.nav-links{left:328px;top:13px;display:flex;gap:30px;font-family:"Roboto",sans-serif;font-size:11px;color:#444}
.nav-links .active{border-bottom:1px solid #444;padding-bottom:8px}
.search{left:1160px;top:12px}
.hero-photo{left:403px;top:40px;width:719px;height:371px;background:linear-gradient(135deg,#d9cfc3,#b9a58d 50%,#7d6b5a)}
.hero-box{left:239px;top:118px;width:360px;height:232px;background:rgba(238,238,238,.93);padding:16px 10px 16px 19px}
.hero-box .kicker{font-size:12.5px;color:#333;white-space:nowrap}
.hero-box h1{font-weight:400;font-size:23.5px;line-height:32px;color:#444;margin-top:6px}
.hero-box .claim{font-style:italic;font-weight:600;color:var(--green);font-size:25px;line-height:32px}
.band{left:0;top:400px}
.step{top:368px;width:205px;height:159px;background:linear-gradient(180deg,#4fb352,#8fd38f 60%,#c7ebc6);border-radius:4px 4px 0 0;color:#fff;text-align:center;font-weight:600;font-size:13px;padding-top:52px;box-shadow:0 2px 4px rgba(0,0,0,.1)}
.step svg{display:block;margin:0 auto 12px}
.chev{top:438px}
.totop{left:1147px;width:40px;height:40px;border-radius:50%;background:#9b9b9b;display:flex;align-items:center;justify-content:center}
.totop.soft{background:#e0e0e0}
.phone-illu{left:311px;top:532px;width:260px;height:332px;background:linear-gradient(150deg,#a9d59f 0%,#8a8a8a 45%,#c9a48e 100%);opacity:.85}
.coach{left:631px;top:580px}
.coach .kicker{font-size:13px;color:#333}
.coach h2{font-weight:400;font-size:24px;line-height:32px;color:#444;margin-top:6px}
.coach h2 em{font-style:italic;font-weight:600;color:var(--green)}
.coach ul{list-style:none;margin-top:22px;font-size:13px;color:#444}
.coach li{height:33px}
.video{left:250px;top:930px;width:699px;height:375px;background:linear-gradient(120deg,#5a5a5a,#b9b2a8 45%,#6b625a);box-shadow:0 2px 8px rgba(0,0,0,.25)}
.divider{left:0;width:1200px;height:2px;background:#e5e5e5;box-shadow:0 1px 3px rgba(0,0,0,.12)}
.center{left:0;width:1200px;text-align:center}
.sec-title{font-weight:400;font-size:24px;color:#444}
.sec-accent{font-style:italic;font-weight:600;font-size:28px;color:var(--green)}
.audience{left:392px;top:1433px;list-style:none;font-size:16px;color:#444}
.audience li{height:31px;display:flex;gap:8px;align-items:center}
.audience li::before{content:"≡";color:var(--green);font-weight:700;font-size:14px}
.tabs{display:flex;font-size:14px;color:#444}
.tabs div{padding:10px 16px;border:1px solid transparent}
.tabs .on{border:1px solid #ddd;border-bottom-color:#fff;background:#fff;border-radius:3px 3px 0 0}
.panel{border:1px solid #ddd;background:#fff}
.lorem{left:275px;top:1728px;width:315px;font-size:13.4px;line-height:20.7px;color:#555}
.media{background:linear-gradient(135deg,#8a7b6a,#d8d2c8 50%,#5b544c)}
.portrait{left:125px;top:2340px;width:400px;height:210px;background:linear-gradient(120deg,#8cc784 0%,#6a6a6a 35%,#b9c4cc 70%,#e7ecef 100%);border-radius:105px;opacity:.85}
.wizard{left:606px;top:2372px;width:337px}
.steps-bar{display:flex;justify-content:space-between;font-size:8px;color:#aaa;position:relative}
.steps-bar span{background:#fff;padding:0 4px;z-index:1;text-align:center;line-height:9px}
.steps-bar .cur{color:var(--green)}
.steps-bar::before{content:"";position:absolute;left:0;right:0;top:6px;height:1px;background:#ddd}
.q{font-size:11px;color:#888;margin-top:22px}
.opts{list-style:none;font-size:13px;color:#555;margin-top:10px}
.opts li{height:21px;display:flex;align-items:center;gap:5px;margin-left:-12px}
.opts li::before{content:"";width:7px;height:7px;border:1px solid #888;border-radius:50%}
.btn{margin-top:6px;height:23px;background:var(--green);color:#fff;text-align:center;font-size:13px;line-height:23px}
.benefits{left:289px;top:2572px;display:flex;gap:28px;font-size:13px;color:#555}
.benefits div{display:flex;align-items:center;gap:7px}
.values{left:257px;top:2785px;font-size:12.2px;line-height:20.7px;color:#444;width:540px}
.footer{left:0;top:3044px;width:1200px;height:297px;background:var(--footer);color:var(--footer-text)}
.footer h3{font-size:17px;font-weight:600;color:#fff}
.fbrand{left:19px;top:60px;display:flex;align-items:center;gap:6px;font-weight:700;font-size:14px;color:#fff}
.fbrand .dot{width:24px;height:24px;border-radius:50%;background:#fff}
.fabout{left:19px;top:105px;font-size:13px;line-height:21px;width:250px}
.social{left:14px;top:170px;display:flex;gap:11px}
.social span{width:14px;height:14px;border-radius:50%;border:1px solid #bbb}
.contact{left:319px;top:25px;font-size:13px;line-height:21px}
.qlinks{left:676px;top:25px}
.qlinks ul{list-style:none;font-size:13px;color:var(--footer-muted);margin-top:14px}
.qlinks li{height:24.5px}
.news{left:918px;top:28px;width:262px;font-size:9px;color:#ccc}
.news .field{height:26px;border-bottom:1px solid #444;padding:5px 12px}
.news .sub{margin-top:16px;height:24px;border:1px solid #ccc;text-align:center;font-size:13px;line-height:22px;color:#fff}
.fline{left:262px;top:3302px;width:676px;height:1px;background:#3c3c3c}
.copy{top:3331px;font-size:7px;color:#888}
</style>
</head>
<body>

<header class="abs nav">
  <div class="abs brand"><span class="dot"></span>PRT DESIGN</div>
  <nav class="abs nav-links">
    <span class="active">Home</span><span>für wen</span><span>kostenloses erstgespräch</span><span>Datenschutz</span><span>prt design</span>
  </nav>
  <svg class="abs search" width="12" height="12" viewBox="0 0 12 12"><circle cx="5" cy="5" r="3.5" fill="none" stroke="#444" stroke-width="1.5"/><line x1="7.6" y1="7.6" x2="10.5" y2="10.5" stroke="#444" stroke-width="1.6"/></svg>
</header>

<div class="abs hero-photo" role="img" aria-label="Foto: junge Familie sitzt im Wohnzimmer unter einem Dach aus Karton"></div>
<svg class="abs band" width="1200" height="40" viewBox="0 0 1200 40"><path d="M0 8 C300 16 900 16 1130 12 C1160 8 1185 4 1200 2 L1200 26 C1185 26 1160 28 1130 30 C900 32 300 32 0 26 Z" fill="var(--green)"/></svg>
<div class="abs hero-box">
  <p class="kicker">Ihre Idee | unser know how | eine perfekte Lösung</p>
  <h1>Wir greifen Ihren Gedanke<br>des Umbaus, Neubaus oder<br>der Sanierung auf und<br>Modelieren</h1>
  <p class="claim">Ihr Gefühl des Einzugs!</p>
</div>

<div class="abs step" style="left:173px"><svg width="34" height="30" viewBox="0 0 34 30" fill="none" stroke="#fff" stroke-width="1.6"><rect x="2" y="2" width="14" height="10" rx="2"/><rect x="18" y="8" width="14" height="10" rx="2"/><circle cx="9" cy="22" r="3"/><circle cx="25" cy="24" r="3"/></svg>Erstgespräch</div>
<div class="abs step" style="left:389px"><svg width="34" height="30" viewBox="0 0 34 30" fill="none" stroke="#fff" stroke-width="1.6"><path d="M3 18 L11 12 L17 16 L23 12 L31 18 L21 26 L13 26 Z"/><path d="M17 2 V8 M10 4 L12 9 M24 4 L22 9"/></svg>Pflichtenheft</div>
<div class="abs step" style="left:606px"><svg width="34" height="30" viewBox="0 0 34 30" fill="none" stroke="#fff" stroke-width="1.6"><circle cx="20" cy="10" r="7"/><path d="M17 17 V22 H23 V17"/><circle cx="9" cy="22" r="4"/></svg>Lastenheft</div>
<div class="abs step" style="left:824px"><svg width="34" height="30" viewBox="0 0 34 30" fill="none" stroke="#fff" stroke-width="1.6"><path d="M3 14 L17 3 L31 14"/><path d="M7 12 V27 H27 V12"/><rect x="14" y="17" width="6" height="10"/></svg>Ihr Einzug</div>
<svg class="abs chev" style="left:364px" width="36" height="36" viewBox="0 0 36 36" fill="none" stroke="#777" stroke-width="3"><path d="M6 6 L18 18 L6 30 M16 6 L28 18 L16 30"/></svg>
<svg class="abs chev" style="left:580px" width="36" height="36" viewBox="0 0 36 36" fill="none" stroke="#777" stroke-width="3"><path d="M6 6 L18 18 L6 30 M16 6 L28 18 L16 30"/></svg>
<svg class="abs chev" style="left:800px" width="30" height="36" viewBox="0 0 30 36" fill="none" stroke="#777" stroke-width="3"><path d="M8 6 L20 18 L8 30"/></svg>

<div class="abs phone-illu" role="img" aria-label="Illustration: Hand hält ein Smartphone mit Raumscan-Ansicht vor grünen und grauen Kreisflächen"></div>

<section class="abs coach">
  <p class="kicker">Baucoaching + RLP-System</p>
  <h2>Wer nicht weiß, was er will,<br>zahlt in der Regel zu <em>viel !“</em></h2>
  <ul><li>Wir planen mit Ihnen Ihr neues Heim.</li><li>Was ist Ihr Ziel?</li><li>Wie soll es fertig aussehen?</li><li>Wann wollen Sie einziehen?</li></ul>
</section>

<div class="abs video" role="img" aria-label="Eingebettete 3D-Raumansicht: Wohnzimmer mit Fenster, Sideboard und Sessel"></div>
<div class="abs" style="left:262px;top:938px;font-size:12px;color:#eee">RAUMSCAN</div>

<div class="abs divider" style="top:1327px"></div>
<h2 class="abs center sec-title" style="top:1344px">Für wen?</h2>
<p class="abs center sec-accent" style="top:1372px">für alle Bauherren und Bauherrinen</p>
<ul class="abs audience">
  <li>für die das Thema neu ist.</li>
  <li>für die, die Kosten im Blick haben.</li>
  <li>für die, die entspannt bauen wollen.</li>
  <li>für die, die sich um das wesentliche kümmern wollen.</li>
</ul>

<div class="abs divider" style="top:1588px"></div>
<h2 class="abs center sec-title" style="top:1608px">Einsatzgebiete</h2>
<div class="abs panel" style="left:250px;top:1703px;width:699px;height:504px"></div>
<div class="abs tabs" style="left:250px;top:1665px"><div class="on">Sanierung</div><div>Neubau</div><div>Umgestaltung</div></div>
<p class="abs lorem">Lorem ipsum dolor sit amet, consetetur sadipscing elitr, sed diam nonumy eirmod tempor invidunt ut labore et dolore magna aliquyam erat, sed diam voluptua. At vero eos et accusam et justo duo dolores et ea rebum. Stet clita kasd gubergren, no sea takimata sanctus est Lorem ipsum dolor sit amet. Lorem ipsum dolor sit amet, consetetur sadipscing elitr, sed diam nonumy eirmod tempor invidunt ut labore et dolore magna aliquyam erat, sed diam voluptua. At vero eos et accusam et justo duo dolores et ea rebum. Stet clita kasd gubergren, no sea takimata sanctus est Lorem ipsum dolor sit amet. Lorem ipsum dolor sit amet, consetetur sadipscing elitr, sed diam nonumy eirmod tempor invidunt ut labore et dolore magna aliquyam erat, sed diam voluptua. At vero eos et accusam et justo duo dolores et ea rebum. Stet clita kasd gubergren, no sea takimata sanctus est Lorem ipsum dolor sit amet.</p>
<div class="abs media" style="left:606px;top:1730px;width:318px;height:179px" role="img" aria-label="Videovorschau: Raumscan im Vergleich zur manuellen Vermessung"></div>
<div class="abs" style="left:644px;top:1743px;font-size:11px;color:#fff">Raumscan: Now Available On Any LiDAR-Enabled i...</div>
<div class="abs" style="left:783px;top:1887px;font-size:12px;color:#fff">Manual Measurement</div>
<svg class="abs" style="left:742px;top:1808px" width="46" height="30" viewBox="0 0 46 30"><rect width="46" height="30" rx="7" fill="#212121" opacity=".85"/><path d="M18 9 L29 15 L18 21 Z" fill="#fff"/></svg>
<div class="abs media" style="left:606px;top:1923px;width:318px;height:212px;background:linear-gradient(135deg,#c9c6c0,#9aa39a 50%,#d7d4cd)" role="img" aria-label="Foto: zwei Bauarbeiter mit Helmen prüfen einen Plan im Rohbau"></div>

<div class="abs divider" style="top:2219px"></div>
<h2 class="abs center sec-title" style="top:2312px">In 4 Schritten zum kostenlosen Erstgespräch</h2>
<div class="abs portrait" role="img" aria-label="Porträtfoto des Baucoachs Jonas Brulin vor grünen und grauen Kreisflächen"></div>
<div class="abs wizard">
  <div class="steps-bar"><span class="cur">aktuelle<br>Situation</span><span>Ihr<br>Vorhaben</span><span>Umfang</span><span>Kontaktdaten</span></div>
  <p class="q">Wie wohnen Sie zurzeit?</p>
  <ul class="opts"><li>Mietwohnung</li><li>Eigentumswohnung</li><li>Mietshaus</li><li>eigenes Haus</li></ul>
  <div class="btn">weiter</div>
</div>
<div class="abs benefits">
  <div><svg width="15" height="15" viewBox="0 0 15 15" fill="none" stroke="var(--green)" stroke-width="1.5"><rect x="1" y="2" width="12" height="12"/><path d="M4 8 L7 11 L14 2"/></svg>Terminverfolgung</div>
  <div><svg width="15" height="15" viewBox="0 0 15 15" fill="none" stroke="var(--green)" stroke-width="1.5"><rect x="1" y="2" width="12" height="12"/><path d="M4 8 L7 11 L14 2"/></svg>Budget kontrolle</div>
  <div><svg width="15" height="15" viewBox="0 0 15 15" fill="none" stroke="var(--green)" stroke-width="1.5"><rect x="1" y="2" width="12" height="12"/><path d="M4 8 L7 11 L14 2"/></svg>gesteigerte Qualität</div>
  <div><svg width="15" height="15" viewBox="0 0 15 15" fill="none" stroke="var(--green)" stroke-width="1.5"><rect x="1" y="2" width="12" height="12"/><path d="M4 8 L7 11 L14 2"/></svg>Bauzeit geniessen</div>
</div>

<div class="abs divider" style="top:2688px"></div>
<div class="abs panel" style="left:244px;top:2768px;width:712px;height:245px"></div>
<div class="abs tabs" style="left:244px;top:2726px;font-size:13.5px"><div class="on">◌ Zukunft Erde</div><div>⚙ Datenschutz</div><div>▮ Backstory</div></div>
<p class="abs values">Dafür stehen wir, bzw.:<br>Warum eigentlich an die Zukunft denken?<br>Wir nutzen nur die Energie, die nötig ist.<br>Wir finden in der Schnittmenge zwischen Mensch und Prozess die größte Effizienz.<br>Wir nutzen die Weisheit, die im Samen jedes Mitarbeiters steckt und erfreuen uns an den<br>Früchten, die durch seine Arbeit entstehen.<br>Wir wachsen im Vertrauen auf unsere Werte und unsere Kunden.<br>Wir glauben an die natürliche Effizienz der Natur.<br>Wir bauen auf das Wissen, welches wir durch stetiges Lernen erweitern, denn das ist die<br>Lösung für ein anhaltenden Wachstum.</p>

<footer class="abs footer">
  <div class="abs fbrand"><span class="dot"></span>PRT DESIGN</div>
  <p class="abs fabout">Lorem ipsum dolor sit amet, consetetur sadipscing elitr, sed diam</p>
  <div class="abs social"><span></span><span></span><span></span><span></span></div>
  <div class="abs contact">
    <h3>Kontakt</h3>
    <p style="margin-top:18px">PRT DESIGN<br>Lindenweg 12<br>78000 Musterstadt</p>
    <p style="margin-top:13px;margin-left:4px">+49 77 00 123 4567<br>Jonas.Brulin@PRT-Design.de</p>
  </div>
  <div class="abs qlinks"><h3>Quick Links</h3><ul><li>Blog</li><li>Project</li><li>Contact us</li><li>Our Team</li></ul></div>
  <div class="abs news"><div class="field">Name</div><div class="field" style="margin-top:14px">Email</div><div class="sub">abonnieren</div></div>
</footer>
<div class="abs fline"></div>
<div class="abs copy" style="left:262px">Copyright © 2021 RV DESIGN. All rights reserved.</div>
<div class="abs copy" style="left:773px;word-spacing:6px">Legal · Terms · GDPR · Usage</div>

<div class="abs totop soft" style="top:468px"><svg width="14" height="9" viewBox="0 0 14 9" fill="none" stroke="#fff" stroke-width="2.5"><path d="M1 8 L7 2 L13 8"/></svg></div>
<div class="abs totop" style="top:732px"><svg width="14" height="9" viewBox="0 0 14 9" fill="none" stroke="#fff" stroke-width="2.5"><path d="M1 8 L7 2 L13 8"/></svg></div>
<div class="abs totop" style="top:1158px"><svg width="14" height="9" viewBox="0 0 14 9" fill="none" stroke="#fff" stroke-width="2.5"><path d="M1 8 L7 2 L13 8"/></svg></div>
<div class="abs totop" style="top:1583px"><svg width="14" height="9" viewBox="0 0 14 9" fill="none" stroke="#fff" stroke-width="2.5"><path d="M1 8 L7 2 L13 8"/></svg></div>
<div class="abs totop" style="top:2007px"><svg width="14" height="9" viewBox="0 0 14 9" fill="none" stroke="#fff" stroke-width="2.5"><path d="M1 8 L7 2 L13 8"/></svg></div>
<div class="abs totop" style="top:2433px"><svg width="14" height="9" viewBox="0 0 14 9" fill="none" stroke="#fff" stroke-width="2.5"><path d="M1 8 L7 2 L13 8"/></svg></div>
<div class="abs totop" style="top:2858px"><svg width="14" height="9" viewBox="0 0 14 9" fill="none" stroke="#fff" stroke-width="2.5"><path d="M1 8 L7 2 L13 8"/></svg></div>
<div class="abs totop" style="top:3282px;background:#3a3a3a"><svg width="14" height="9" viewBox="0 0 14 9" fill="none" stroke="#222" stroke-width="2.5"><path d="M1 8 L7 2 L13 8"/></svg></div>

</body>
</html>
```